My Book needs a front and back cover design

I need you to design my front and back cover of my book. The title of my book is : Lanterns Past Harbour
Tide Notes
7 paths to gardening calmly always

The picture that I uploaded needs to be on the front cover. On the back cover it should be excerpt from Chapter One like this :

As years have gone by I have become much more conscious about my problem with stuttering, more able to relax my muscles to alleviate it. At the age of 20, I realized that stuttering is like a demon in my head that needs to be killed and that nothing is wrong with me. Furthermore, no one can help me but myself. I'm holding the key of my future. Everything is just in my head.

With this book, I want to help you realize that nobody can help you fix your stuttering better than yourself. There's no quick-get-rid-of-stuttering cure. The cure lies inside of you.

- Lorcan Vittel, excerpt from Chapter One
----------------------------------------------------------------------------------

My name also needs to be located on the front cover.

Target Market(s)

80 million people who stutter each day

Industry/Entity Type

Psychology

Font styles to use
Serif
Sans Serif

Colors
1b1b1b
000000
333333

Requirements
Must have
• Front Cover : Full Title and subtitle and my name and my picture
• Back Cover : Excerpt from my Chapter One with my name below just as I have described in my project description
Nice to have
• Maybe black background would be the best for the front cover.

```html
<!DOCTYPE html>
<html lang="en">
<head>
<meta charset="utf-8">
<title>Lanterns Past Harbour – Book Covers</title>
<link rel="stylesheet" href="https://fonts.googleapis.com/css2?family=Merriweather:wght@900&family=Tinos:wght@700&family=Caveat:wght@500&family=Arimo:wght@700&display=swap">
<style>
  :root {
    --stage-light: #ededed;
    --stage-dark: #5f5f5f;
    --cover-black: #000000;
    --cover-charcoal: #1b1b1b;
    --cover-grey: #333333;
    --text-white: #ffffff;
    --frame-cyan: #2fd3da;
  }
  * { margin: 0; padding: 0; box-sizing: border-box; }
  html, body { width: 1200px; height: 1200px; overflow: hidden; }
  body {
    position: relative;
    background: linear-gradient(90deg, var(--stage-light) 0%, var(--stage-dark) 100%);
  }
  .cover {
    position: absolute;
    top: 259px;
    width: 453px;
    height: 680px;
    background: var(--cover-black);
    overflow: hidden;
    box-shadow: 4px 6px 8px rgba(0,0,0,0.45);
    color: var(--text-white);
  }
  .cover--back { left: 110px; }
  .cover--front { left: 638px; }
  .cover__swoosh { position: absolute; inset: 0; width: 100%; height: 100%; }
  .cover__footer {
    position: absolute; left: 0; right: 0; bottom: 0; height: 38px;
    background: var(--cover-charcoal);
  }

  /* Back cover */
  .excerpt {
    position: absolute; left: 44px; top: 57px; width: 374px;
    font-family: "Tinos", "Times New Roman", serif;
    font-weight: 700; font-size: 13.6px; line-height: 22px;
  }
  .excerpt__label { margin-bottom: 22px; }
  .excerpt__author {
    float: left; width: 143px; margin-right: 0; text-align: center;
  }
  .excerpt__portrait {
    display: block; width: 127px; height: 137px; margin: 2px 0 0 3px;
    border: 2px solid var(--frame-cyan);
    background: radial-gradient(ellipse at 50% 45%, #3a3a3a 0%, #141414 70%);
  }
  .excerpt__caption { margin-top: 10px; padding-left: 2px; }
  .excerpt__body p { margin-bottom: 22px; }
  .excerpt__sign { text-align: right; margin-top: 44px; }

  /* Front cover */
  .front__photo {
    position: absolute; left: 0; right: 0; top: 118px; bottom: 38px;
    background: radial-gradient(ellipse at 50% 35%, #2e2e2e 0%, #151515 45%, #000 80%);
  }
  .front__title {
    position: absolute; left: 0; right: 0; top: 10px; text-align: center;
    font-family: "Merriweather", Georgia, serif; font-weight: 900;
    font-size: 50px; line-height: 62px; letter-spacing: -0.5px;
  }
  .front__title-script {
    position: absolute; left: 0; right: 0; top: 72px; text-align: center;
    font-family: "Caveat", cursive; font-weight: 500; font-size: 44px; line-height: 44px;
  }
  .front__series {
    position: absolute; left: 0; right: 0; top: 494px; text-align: center;
    font-family: "Tinos", "Times New Roman", serif; font-weight: 700; font-size: 32px;
  }
  .front__tagline {
    position: absolute; left: 0; right: 0; top: 545px; text-align: center;
    font-family: "Arimo", Arial, sans-serif; font-weight: 700; font-size: 17px; line-height: 30px;
  }
  .front__author {
    position: absolute; left: 0; right: 0; top: 610px; text-align: center;
    font-family: "Arimo", Arial, sans-serif; font-weight: 700; font-size: 12.5px;
  }
</style>
</head>
<body>

<section class="cover cover--back">
  <svg class="cover__swoosh" viewBox="0 0 453 680" preserveAspectRatio="none" aria-hidden="true">
    <rect width="453" height="680" fill="var(--cover-black)"/>
    <path d="M0 0 H453 V60 C330 70 150 120 0 170 Z" fill="var(--cover-charcoal)"/>
  </svg>
  <div class="excerpt">
    <p class="excerpt__label">Excerpt from Chapter One like this :</p>
    <div class="excerpt__author">
      <div class="excerpt__portrait" role="img" aria-label="Portrait photo of the author"></div>
      <p class="excerpt__caption">Lorcan Vittel,</p>
    </div>
    <div class="excerpt__body">
      <p>As years have gone by I have become much more conscious about my problem with stuttering, more able to relax my muscles to alleviate it. At the age of 20, I realized that stuttering is like a demon in my head that needs to be killed and that nothing is wrong with me. Furthermore, no one can help me but myself. I’m holding the key of my future.<br>Everything is just in my head.</p>
      <p>With this book, I want to help you realize that nobody can help you fix your stuttering better than yourself. There’s no quick-get-rid-of-stuttering cure. The cure lies inside of you.</p>
    </div>
    <p class="excerpt__sign">- Lorcan Vittel,<br>excerpt from Chapter One</p>
  </div>
  <div class="cover__footer"></div>
</section>

<section class="cover cover--front">
  <svg class="cover__swoosh" viewBox="0 0 453 680" preserveAspectRatio="none" aria-hidden="true">
    <rect width="453" height="680" fill="var(--cover-black)"/>
    <path d="M0 0 H453 V170 C300 120 120 70 0 60 Z" fill="var(--cover-charcoal)"/>
  </svg>
  <div class="front__photo" role="img" aria-label="Photo of the author in a black polo shirt against a dark backdrop"></div>
  <h1 class="front__title">Lanterns Past</h1>
  <p class="front__title-script">Harbour</p>
  <h2 class="front__series">Tide Notes</h2>
  <p class="front__tagline">7 paths to gardening<br>calmly always</p>
  <p class="front__author">- Lorcan Vittel</p>
  <div class="cover__footer"></div>
</section>

</body>
</html>
```